Business card for law firm

Need business card for new law firm. Think confident, authoritative, conservative, but not stuffy or old-fashioned.

Contact Information for Business Card

Content for card - logo (uploaded), plus the following:

Paul Wexbury (larger font)
Managing Partner (larger font, but not as large as name)
Level 9, 41 Tansy Lane
Sydney NSW 2000
Main Tel 02 7346 2190
Direct Tel 02 6273 4415
Email paul@qvlegal.com.au
www.qvlegal.com.au

Letterhead design should include logo plus:
Level 9, 41 Tansy Lane
Sydney NSW 2000
Tel 02 6273 4415
www.qvlegal.com.au

```html
<!DOCTYPE html>
<html lang="en">
<head>
<meta charset="utf-8">
<title>Quayvale Legal – Business Card</title>
<link href="https://fonts.googleapis.com/css2?family=Jost:wght@400;500&family=Roboto:wght@400;700&display=swap" rel="stylesheet">
<style>
  :root {
    --backdrop: #9c9c9c;
    --navy: #0f1d57;
    --navy-deep: #0a1745;
    --navy-light: #13246a;
    --paper: #e6e6e6;
    --ink: #1c1c1c;
    --white: #ffffff;
  }
  * { margin: 0; padding: 0; box-sizing: border-box; }
  html, body {
    width: 1200px;
    height: 1000px;
    overflow: hidden;
  }
  body {
    background: var(--backdrop);
    position: relative;
    font-family: "Jost", sans-serif;
  }
  .card {
    position: absolute;
    top: 207px;
    width: 352px;
    height: 586px;
  }
  .card-front {
    left: 200px;
    background: linear-gradient(160deg, var(--navy-light) 0%, var(--navy-deep) 45%, var(--navy) 70%, var(--navy-deep) 100%);
  }
  .card-front .brand {
    position: absolute;
    left: 0;
    right: 0;
    top: 318px;
    text-align: center;
    color: var(--white);
    font-family: "Jost", sans-serif;
    font-weight: 400;
    font-size: 34px;
    letter-spacing: 3px;
    text-transform: uppercase;
    line-height: 1.2;
  }
  .card-back {
    left: 635px;
    background: var(--paper);
    color: var(--ink);
  }
  .person-name {
    position: absolute;
    left: 39px;
    top: 38px;
    font-family: "Roboto", sans-serif;
    font-weight: 700;
    font-size: 24px;
    color: var(--navy);
    text-transform: uppercase;
    letter-spacing: 0.2px;
  }
  .person-role {
    position: absolute;
    left: 39px;
    top: 69px;
    font-family: "Roboto", sans-serif;
    font-size: 17px;
    color: #2a2a2a;
  }
  .address, .phones, .web {
    position: absolute;
    left: 39px;
    font-size: 14px;
    line-height: 20px;
    letter-spacing: 0.3px;
  }
  .address { top: 123px; }
  .phones { top: 186px; }
  .phones .label { color: var(--navy); font-weight: 500; }
  .web { top: 250px; }
  .web li {
    list-style: none;
    display: flex;
    align-items: center;
    gap: 6px;
  }
  .web svg { width: 11px; height: 11px; }
  .web strong { font-weight: 500; color: var(--navy); }
  .back-brand {
    position: absolute;
    right: 28px;
    bottom: 22px;
    display: flex;
    align-items: flex-end;
    gap: 12px;
  }
  .back-brand .brand-name {
    font-family: "Jost", sans-serif;
    font-weight: 400;
    font-size: 14px;
    letter-spacing: 2px;
    text-transform: uppercase;
    color: var(--navy);
  }
  .back-brand .brand-square {
    width: 124px;
    height: 124px;
    background: var(--navy);
  }
</style>
</head>
<body>
  <section class="card card-front" aria-label="Card front">
    <div class="brand">Quayvale<br>Legal</div>
  </section>

  <section class="card card-back" aria-label="Card back">
    <h1 class="person-name">Paul Wexbury</h1>
    <p class="person-role">Managing Partner</p>

    <p class="address">Level 9, 41 Tansy Lane<br>Sydney NSW 2000</p>

    <p class="phones">
      <span class="label">Main Tel</span> 02 7346 2190<br>
      <span class="label">Direct Tel</span> 02 6273 4415
    </p>

    <ul class="web">
      <li>
        <svg viewBox="0 0 12 12" aria-hidden="true"><rect x="1" y="2.5" width="10" height="7" fill="var(--navy)"/><path d="M1 2.5 L6 6.5 L11 2.5" stroke="#fff" stroke-width="1" fill="none"/></svg>
        paul@qvlegal.com.au
      </li>
      <li>
        <svg viewBox="0 0 12 12" aria-hidden="true"><circle cx="6" cy="6" r="5" fill="none" stroke="var(--navy)" stroke-width="1.2"/><ellipse cx="6" cy="6" rx="2.2" ry="5" fill="none" stroke="var(--navy)" stroke-width="1"/><line x1="1" y1="6" x2="11" y2="6" stroke="var(--navy)" stroke-width="1"/></svg>
        <span>www.<strong>qvlegal.com.au</strong></span>
      </li>
    </ul>

    <div class="back-brand">
      <span class="brand-name">Quayvale Legal</span>
      <span class="brand-square" aria-hidden="true"></span>
    </div>
  </section>
</body>
</html>
```